Letterhead and Business card for Construction company

We need a letterhead and business card with our new company logo. We are based in NY. We develop and build properties.

The design should incorporate some unique feature from the logo (shape, font...). it should look like an extension from it.

Design should be clean and elegant, professional, not too busy.

The letterhead should include:
Logo (attached)
Address
Phone
Email

Please find the attached logo images and AI file.

Target Market(s)

Construction industry professionals

Industry/Entity Type

Construction, Development

Font styles to use
Sans Serif

Colors

Designer to choose colors to be used in the design.

Requirements
Must have
• Design should incorporate logo elements, additional assets are welcome. I'd like to see some other shapes / images invorporated too.

```html
<!DOCTYPE html>
<html lang="en">
<head>
<meta charset="utf-8">
<title>Halvern Building – Business Card</title>
<link href="https://fonts.googleapis.com/css2?family=Montserrat:wght@600;700&family=Roboto:wght@400&display=swap" rel="stylesheet">
<style>
  :root {
    --stage: #2b2b2b;
    --card-dark: #2f2f2f;
    --card-dark-edge: #1e1e1e;
    --card-light: #ffffff;
    --ink: #2a2a2a;
    --ink-soft: #6b6b6b;
    --accent: #f47a20;
    --band-dark: #1c1c1c;
    --tower-light: #9a9a9a;
    --tower-dark: #3a3a3a;
  }
  * { box-sizing: border-box; margin: 0; padding: 0; }
  html, body { width: 1200px; height: 929px; overflow: hidden; }
  body {
    background: var(--stage);
    position: relative;
    font-family: "Roboto", Arial, sans-serif;
  }
  .card {
    position: absolute;
    width: 540px;
    height: 309px;
    border-radius: 4px;
    overflow: hidden;
    box-shadow: 0 10px 30px rgba(0,0,0,.45);
  }

  /* Back side */
  .card--back {
    left: 90px;
    top: 100px;
    background: linear-gradient(160deg, var(--card-dark) 0%, var(--card-dark-edge) 100%);
  }
  .card--back .skyline-art {
    position: absolute;
    left: 0;
    bottom: 0;
    width: 300px;
    height: 250px;
    background: linear-gradient(115deg, var(--tower-light) 0%, var(--tower-dark) 85%);
    opacity: .55;
  }
  .card--back .brand-name {
    position: absolute;
    right: 44px;
    top: 100px;
    color: #ffffff;
    font-family: "Montserrat", Arial, sans-serif;
    font-weight: 700;
    font-size: 30px;
    letter-spacing: 1px;
    text-align: right;
    line-height: 1.1;
  }

  /* Front side */
  .card--front {
    left: 570px;
    top: 500px;
    background: var(--card-light);
  }
  .card--front .brand-name {
    position: absolute;
    right: 40px;
    top: 40px;
    color: var(--ink);
    font-family: "Montserrat", Arial, sans-serif;
    font-weight: 700;
    font-size: 30px;
    letter-spacing: 1px;
    text-align: right;
    line-height: 1.1;
  }
  .person {
    position: absolute;
    left: 34px;
    right: 34px;
    top: 126px;
  }
  .person__header {
    display: flex;
    align-items: flex-end;
  }
  .person__name {
    flex: none;
    font-family: "Montserrat", Arial, sans-serif;
    font-weight: 700;
    font-size: 17px;
    line-height: 20px;
    color: var(--ink);
    text-transform: uppercase;
    letter-spacing: .3px;
  }
  .person__rule {
    flex: 1;
    height: 1.5px;
    margin: 0 0 1px 14px;
    background: var(--accent);
  }
  .person__role {
    font-family: "Montserrat", Arial, sans-serif;
    font-weight: 600;
    font-size: 16px;
    color: var(--accent);
    margin-top: 2px;
  }
  .contacts {
    position: absolute;
    left: 34px;
    top: 190px;
    list-style: none;
  }
  .contacts li {
    display: flex;
    align-items: center;
    gap: 8px;
    font-size: 13.5px;
    color: var(--ink-soft);
    line-height: 22px;
  }
  .contacts svg { width: 13px; height: 13px; flex: none; }
  .address {
    position: absolute;
    right: 40px;
    top: 170px;
    font-size: 13.5px;
    color: var(--ink-soft);
    text-align: right;
    line-height: 20px;
  }
  .bottom-band {
    position: absolute;
    left: 0;
    bottom: 0;
    width: 100%;
    height: 22px;
  }
</style>
</head>
<body>

  <section class="card card--back" aria-label="Business card back">
    <div class="skyline-art" role="img" aria-label="Stylised grey skyline of tower shapes"></div>
    <div class="brand-name">HALVERN<br>BUILDING</div>
  </section>

  <section class="card card--front" aria-label="Business card front">
    <div class="brand-name">HALVERN<br>BUILDING</div>

    <div class="person">
      <div class="person__header">
        <p class="person__name">Marten L. Osgood</p>
        <span class="person__rule" aria-hidden="true"></span>
      </div>
      <p class="person__role">Brand Master</p>
    </div>

    <ul class="contacts">
      <li>
        <svg viewBox="0 0 16 16" aria-hidden="true"><path fill="#f47a20" d="M3 1h3l1.5 4-2 1.3a9 9 0 0 0 4.2 4.2L11 8.5l4 1.5v3a2 2 0 0 1-2 2A13 13 0 0 1 1 3a2 2 0 0 1 2-2z"/></svg>
        1-888-555-0174
      </li>
      <li>
        <svg viewBox="0 0 16 16" aria-hidden="true"><rect x="1" y="3" width="14" height="10" fill="#f47a20"/><path d="M1 3l7 6 7-6" fill="none" stroke="#fff" stroke-width="1.4"/></svg>
        info@halvernbuild.com
      </li>
      <li>
        <svg viewBox="0 0 16 16" aria-hidden="true"><circle cx="8" cy="8" r="7" fill="#f47a20"/><path d="M1 8h14M8 1c-3 3.5-3 10.5 0 14M8 1c3 3.5 3 10.5 0 14" fill="none" stroke="#fff" stroke-width="1"/></svg>
        www.halvernbuild.com
      </li>
    </ul>

    <p class="address">48 Larkspur Ave Suite<br>7 Ridgefield NY 10590</p>

    <svg class="bottom-band" viewBox="0 0 540 22" preserveAspectRatio="none" aria-hidden="true">
      <polygon points="0,22 0,16 360,16 356,22" fill="var(--band-dark)"/>
      <polygon points="362,22 370,0 540,0 540,22" fill="var(--accent)"/>
    </svg>
  </section>

</body>
</html>
```